TRU PEAK POWER.

I'd like my business logo.
contact name: Desmond Halvik
phone:0438275160
email: info@trupeakpower.net.au
website: www.trupeakpower.net.au

services:
solar
battery storage
LED lighting
energy saving solutions
general electrical
I'd like the design to look professional

Target Market(s)

Everyone

Industry/Entity Type

Business

Contact Information for Business Card

as described above

Requirements
Must have
• Id like the colours and the design to work well with my logo.

```html
<!DOCTYPE html>
<html lang="en">
<head>
<meta charset="utf-8">
<title>Tru Peak Power – Business Card</title>
<link rel="stylesheet" href="https://fonts.googleapis.com/css2?family=Roboto+Condensed:wght@400;700&display=swap">
<style>
  :root {
    --orange: #f47300;
    --white: #ffffff;
    --green: #5fb562;
    --lime: #8ab814;
    --brand-green: #47a24a;
    --ink: #111111;
  }
  * { margin: 0; padding: 0; box-sizing: border-box; }
  html, body { width: 1200px; height: 800px; overflow: hidden; background: var(--white); }
  .card {
    position: relative;
    width: 1200px;
    height: 800px;
    overflow: hidden;
    font-family: "Roboto Condensed", "Arial Narrow", sans-serif;
    background: var(--white);
  }
  .top-band {
    position: absolute; left: 0; top: 0;
    width: 1200px; height: 120px;
    background: var(--orange);
  }
  .brand {
    position: absolute; left: 72px; top: 210px;
    display: flex; align-items: center; gap: 22px;
  }
  .brand-dot {
    width: 64px; height: 64px; border-radius: 50%;
    background: var(--orange);
  }
  .brand-name {
    font-size: 64px; font-weight: 700; letter-spacing: 1px;
    color: var(--brand-green);
    line-height: 1;
  }
  .services {
    position: absolute; left: 741px; top: 158px;
    list-style: none;
    color: var(--orange);
    font-size: 41px; font-weight: 400;
    line-height: 53.5px;
  }
  .lower {
    position: absolute; left: 0; top: 407px;
    width: 1200px; height: 393px;
  }
  .lower svg { display: block; }
  .name-tab {
    position: absolute; left: 573px; top: 407px;
    width: 627px; height: 144px;
    background: var(--orange);
    border-bottom-left-radius: 144px 144px;
  }
  .contact-name {
    position: absolute; right: 45px; top: 425px;
    color: var(--white);
    font-size: 82px; font-weight: 400;
    line-height: 1;
  }
  .contacts {
    position: absolute; left: 104px; top: 533px;
    list-style: none;
    color: var(--white);
    font-size: 38px;
  }
  .contacts li {
    display: flex; align-items: center;
    height: 50px; margin-bottom: 14px;
  }
  .contacts li:nth-child(2) { margin-top: 6px; margin-bottom: 10px; }
  .contacts .icon { width: 46px; height: 46px; margin-right: 16px; flex: none; }
  .contacts li:not(:first-child) .icon { margin-right: 24px; }
</style>
</head>
<body>
<div class="card">
  <div class="top-band"></div>

  <div class="brand">
    <span class="brand-dot"></span>
    <span class="brand-name">TRU PEAK POWER</span>
  </div>

  <ul class="services">
    <li>Solar</li>
    <li>Battery Storage</li>
    <li>LED Lighting</li>
    <li>Energy Saving Solutions</li>
  </ul>

  <div class="lower">
    <svg width="1200" height="393" viewBox="0 0 1200 393">
      <rect width="1200" height="393" fill="var(--green)"/>
      <path d="M0 220 C 300 205, 620 345, 930 335 C 1060 330, 1150 292, 1200 273 L1200 393 L0 393 Z" fill="var(--lime)"/>
    </svg>
  </div>

  <div class="name-tab"></div>
  <div class="contact-name">Desmond Halvik</div>

  <ul class="contacts">
    <li>
      <svg class="icon" viewBox="0 0 24 24"><path fill="var(--ink)" d="M6.6 10.8c1.4 2.8 3.8 5.1 6.6 6.6l2.2-2.2c.3-.3.7-.4 1-.2 1.1.4 2.3.6 3.6.6.6 0 1 .4 1 1V20c0 .6-.4 1-1 1C10.6 21 3 13.4 3 4c0-.6.4-1 1-1h3.5c.6 0 1 .4 1 1 0 1.3.2 2.5.6 3.6.1.3 0 .7-.2 1z"/></svg>
      <span>0438275160</span>
    </li>
    <li>
      <svg class="icon" viewBox="0 0 24 24"><rect x="2.5" y="5" width="19" height="14" fill="none" stroke="var(--ink)" stroke-width="1.6"/><path d="M2.5 5 L12 13 L21.5 5 M2.5 19 L9.5 11.5 M21.5 19 L14.5 11.5" fill="none" stroke="var(--ink)" stroke-width="1.6"/></svg>
      <span>info@trupeakpower.net.au</span>
    </li>
    <li>
      <svg class="icon" viewBox="0 0 24 24"><g fill="none" stroke="var(--ink)" stroke-width="1.6"><circle cx="12" cy="12" r="9.5"/><ellipse cx="12" cy="12" rx="4.2" ry="9.5"/><path d="M2.5 12h19M4 7h16M4 17h16M12 2.5v19"/></g></svg>
      <span>www.trupeakpower.net.au</span>
    </li>
  </ul>
</div>
</body>
</html>
```